Family Medicine Business Card Design Project

Looking for a very professional, clean, simple, minimalist, well designed business card.

I am reestablishing my medical practice in a new town and looking for a new look. I am currently in the process of revising my corporate identity. I recently changed the business name to Clear Path Family Medicine and had the logo redesigned.

You can visit the website http://cleerpathfm.net/ to get a feel for what I may be looking for.

I am looking for a two sided business card.
I would like to include an appointment reminder on one side.
Colors would ideally be greens and blues, cool tones, or graytones.

I like the idea of including a QR code but only if able to do in a clean and simple design.

Things to include on business card
Noel Brandt, D.O.
Clear Path Family Medicine
4710 Harlow Bend
Brookdale, TX 79345
Phone: 806-472-7284 (PATH)
Fax: 806-472-3815
Web: cleerpathfm.net
friendspace.net/ClearPathFamilyMedicine
Email:info@cleerpathfm.net

Somehow list/bullets of, or specializing in:
Nutrition
Manipulation
Acupuncture
Prolotherapy
Functional Medicine

May include slogan
"Helping you to live a clear path"

I have attached the logo design, and other samples I have seen that have features that I may be looking for.

Reason: I apologize for extending the deadline, we are packing and moving tomorrow and I will not have internet for 3 day, I still need to give feedback and waiting on several revisions. I promise I will not extend deadline again.

Target Market(s)

Health conscious people of all ages looking for a family medicine doctor

Industry/Entity Type

Medical

Requirements
Must have
• I am looking for a two sided business card.
Nice to have
• Colors would ideally be greens and blues or graytones.

May include slogan

```html
<!DOCTYPE html>
<html lang="en">
<head>
<meta charset="utf-8">
<title>Clear Path Family Medicine – Business Card</title>
<link rel="stylesheet" href="https://fonts.googleapis.com/css2?family=Mulish:wght@400;600;800&display=swap">
<style>
  :root{
    --bg:#d9d9d9;
    --blue-deep:#0f4e7a;
    --blue-mid:#1d6e9e;
    --blue-light:#3a8fbe;
    --band:#2f86b8;
    --panel:#0f4a6e;
    --green:#7cc142;
    --paper:#ebebeb;
    --ink:#333333;
    --white:#ffffff;
  }
  *{box-sizing:border-box;margin:0;padding:0}
  html,body{width:1200px;height:1013px;overflow:hidden}
  body{background:var(--bg);font-family:"Mulish",sans-serif;position:relative}

  .card{position:absolute;left:250px;width:700px;height:400px;overflow:hidden;
        box-shadow:0 6px 18px rgba(0,0,0,.18)}

  /* Front */
  .card-front{top:70px;
    background:linear-gradient(160deg,var(--blue-light) 0%,var(--blue-mid) 45%,var(--blue-deep) 100%);
    display:flex;align-items:center;justify-content:center}
  .brand-front{display:flex;align-items:center;gap:18px;color:var(--white)}
  .brand-front .brand-dot{width:46px;height:46px;border-radius:50%;background:var(--white)}
  .brand-front .brand-name{font-weight:800;font-size:50px;line-height:1}
  .brand-front .brand-sub{font-weight:800;font-size:19px;letter-spacing:7px;margin-top:8px}

  /* Back */
  .card-back{top:540px;background:var(--blue-mid)}
  .back-top{position:absolute;left:0;top:0;width:700px;height:122px;background:var(--paper);
            border-bottom:5px solid var(--green)}
  .brand-back{position:absolute;left:32px;top:30px;display:flex;align-items:center;gap:12px;color:var(--ink)}
  .brand-back .brand-dot{width:30px;height:30px;border-radius:50%;background:var(--ink)}
  .brand-back .brand-name{font-weight:800;font-size:34px;line-height:1}
  .brand-back .brand-sub{font-weight:800;font-size:12.5px;letter-spacing:5px;margin-top:5px}

  .doctor{position:absolute;left:440px;top:26px;color:var(--ink)}
  .doctor-name{font-weight:800;font-size:24px;margin-bottom:6px}
  .doctor-line{font-size:12.5px;display:flex;align-items:center;gap:6px;line-height:16px}
  .doctor-line svg{width:10px;height:10px;flex:none}
  .doctor-line.indent{padding-left:16px}

  .back-body{position:absolute;left:0;top:127px;width:700px;height:230px;
             background:linear-gradient(170deg,var(--blue-light),var(--blue-mid) 60%,var(--blue-deep))}
  .contacts{position:absolute;left:32px;top:34px;color:var(--white);font-size:13px;list-style:none}
  .contacts li{display:flex;align-items:center;gap:8px;line-height:18px}
  .contacts svg{width:10px;height:10px;flex:none}
  .fax{position:absolute;left:248px;top:34px;color:var(--white);font-size:13px;display:flex;align-items:center;gap:8px;line-height:18px}
  .fax svg{width:10px;height:10px}

  .reminder{position:absolute;left:442px;top:150px;width:230px;height:168px;border-radius:14px;
            background:var(--panel);padding:12px 16px;color:var(--white)}
  .reminder h3{font-weight:600;font-size:13px;letter-spacing:1px;text-align:center;margin-bottom:8px}
  .field{display:flex;align-items:center;gap:8px;margin-bottom:8px}
  .field label{width:40px;text-align:right;font-weight:800;font-size:12px}
  .field span{flex:1;height:22px;border-radius:8px;background:var(--white)}

  .services{position:absolute;left:0;bottom:0;width:700px;height:43px;background:var(--band);
            color:var(--white);font-size:11.5px;letter-spacing:1px;text-transform:uppercase;
            display:flex;align-items:center;justify-content:center;gap:10px}
</style>
</head>
<body>

<section class="card card-front" aria-label="Card front">
  <div class="brand-front">
    <span class="brand-dot"></span>
    <div>
      <div class="brand-name">Clear Path</div>
      <div class="brand-sub">FAMILY MEDICINE</div>
    </div>
  </div>
</section>

<section class="card card-back" aria-label="Card back">
  <div class="back-top">
    <div class="brand-back">
      <span class="brand-dot"></span>
      <div>
        <div class="brand-name">Clear Path</div>
        <div class="brand-sub">FAMILY MEDICINE</div>
      </div>
    </div>
    <div class="doctor">
      <div class="doctor-name">Noel Brandt, D.O.</div>
      <div class="doctor-line">
        <svg viewBox="0 0 10 10"><circle cx="5" cy="3" r="2.2" fill="#7cc142"/><path d="M1 10a4 4 0 0 1 8 0z" fill="#7cc142"/></svg>
        Clear Path Family Medicine
      </div>
      <div class="doctor-line">
        <svg viewBox="0 0 10 10"><path d="M5 0a3.5 3.5 0 0 1 3.5 3.5C8.5 6 5 10 5 10S1.5 6 1.5 3.5A3.5 3.5 0 0 1 5 0z" fill="#7cc142"/><circle cx="5" cy="3.5" r="1.2" fill="#ebebeb"/></svg>
        4710 Harlow Bend
      </div>
      <div class="doctor-line indent">Brookdale, TX 79345</div>
    </div>
  </div>

  <div class="back-body">
    <ul class="contacts">
      <li><svg viewBox="0 0 10 10"><path d="M2 0l2 2.5-1 1.3a6 6 0 0 0 3.2 3.2l1.3-1L10 8l-1.5 2C4 10 0 6 0 1.5z" fill="#7cc142"/></svg>806-472-7284 (PATH)</li>
      <li><svg viewBox="0 0 10 10"><circle cx="5" cy="5" r="4.3" fill="none" stroke="#7cc142" stroke-width="1.3"/><path d="M.7 5h8.6M5 .7c-2.5 2.6-2.5 6 0 8.6M5 .7c2.5 2.6 2.5 6 0 8.6" fill="none" stroke="#7cc142"/></svg>cleerpathfm.net</li>
      <li><svg viewBox="0 0 10 10"><circle cx="5" cy="5" r="4.5" fill="#7cc142"/></svg>friendspace.net/ClearPathFamilyMedicine</li>
      <li><svg viewBox="0 0 10 10"><rect x="0" y="1.5" width="10" height="7" fill="#7cc142"/><path d="M0 1.5l5 4 5-4" fill="none" stroke="#1d6e9e"/></svg>info@cleerpathfm.net</li>
    </ul>
    <div class="fax">
      <svg viewBox="0 0 10 10"><rect x="0" y="3" width="10" height="6" rx="1" fill="#7cc142"/><rect x="2.5" y="0" width="5" height="4" fill="#7cc142"/></svg>
      806-472-3815
    </div>
  </div>

  <div class="reminder">
    <h3>APPOINTMENT REMINDER</h3>
    <div class="field"><label>Dr.</label><span></span></div>
    <div class="field"><label>Day</label><span></span></div>
    <div class="field"><label>Date</label><span></span></div>
    <div class="field"><label>Time</label><span></span></div>
  </div>

  <div class="services">
    <span>Nutrition</span><span>·</span><span>Manipulation</span><span>·</span><span>Acupuncture</span><span>·</span><span>Prolotherapy</span><span>·</span><span>Functional Medicine</span>
  </div>
</section>

</body>
</html>
```